Business Cards Needed For Veterinary Business

Looking for a business card design for a veterinary blood bank. We would like it to be clean and professional on appearance but still warm and inviting. We would like to utilize our logo and similar coloring. We will use our phone number, email, website, employee name, employee title.

We do not want a bunch of animated animal photos but do not need the style to be as clinical as a laboratory or human medical procedure office.

We are looking for some creative ideas to choose from so that we can generate a standout professional business card for our management team to utilize.

Target Market(s)

professionals

Industry/Entity Type

veterinary

Contact Information for Business Card

employee name, employee title, phone number, website URL, email

Font styles to use
Sans Serif

Colors
0054AA
0677BA
7BADD7
CADEEF
E8F1F8
EB3D1F
EC4F4E
F09395
F8D3D4
FCEDEE

Requirements
Nice to have
• creative design
Should not have
• animated photos

```html
<!DOCTYPE html>
<html lang="en">
<head>
<meta charset="utf-8">
<title>Pinecrest Animal Transfusion Service – Business Card</title>
<link rel="stylesheet" href="https://fonts.googleapis.com/css2?family=Montserrat:wght@600;700;800&family=Open+Sans:wght@400;600&display=swap">
<style>
  :root {
    --blue-deep: #0054AA;
    --blue-mid: #0677BA;
    --blue-soft: #7BADD7;
    --blue-pale: #E8F1F8;
    --red: #EB3D1F;
    --red-pale: #FCEDEE;
    --ink: #3a3f47;
    --paper: #ffffff;
    --stage: #d9dce1;
  }
  * { box-sizing: border-box; margin: 0; padding: 0; }
  html, body { width: 1200px; height: 913px; overflow: hidden; }
  body {
    background: var(--stage);
    position: relative;
    font-family: "Open Sans", Arial, sans-serif;
  }
  .card {
    position: absolute;
    width: 560px;
    height: 320px;
    border-radius: 18px;
    overflow: hidden;
    box-shadow: 0 14px 30px rgba(0,0,0,.25);
  }

  /* back side */
  .card-back { left: 70px; top: 90px; background: var(--blue-deep); }
  .card-back .pattern {
    position: absolute; inset: 0;
    background: linear-gradient(135deg, var(--blue-deep) 0%, var(--blue-mid) 100%);
  }
  .back-mark {
    position: absolute; right: 44px; top: 120px;
    display: flex; align-items: center; gap: 6px;
    font-family: "Montserrat", Arial, sans-serif;
    font-weight: 700; font-size: 14px; color: var(--paper);
  }
  .back-mark .dot { width: 10px; height: 10px; border-radius: 50%; background: var(--red); }

  /* front side */
  .card-front { left: 570px; top: 500px; background: var(--paper); }
  .edge-tab {
    position: absolute; left: -14px; top: 196px;
    width: 28px; height: 40px; border-radius: 10px;
    background: var(--blue-deep);
  }
  .brand { position: absolute; left: 40px; top: 40px; }
  .brand-row { display: flex; align-items: center; gap: 10px; }
  .brand-dot { width: 30px; height: 30px; border-radius: 50%; background: var(--red); }
  .brand-name {
    font-family: "Montserrat", Arial, sans-serif;
    font-weight: 700; font-size: 34px; line-height: 1; color: var(--blue-deep);
  }
  .brand-full {
    font-family: "Montserrat", Arial, sans-serif;
    font-weight: 600; font-size: 10.5px; color: var(--ink);
    margin-top: 8px; letter-spacing: 1px; text-transform: uppercase;
  }
  .person { position: absolute; left: 40px; top: 150px; }
  .person-name {
    font-family: "Montserrat", Arial, sans-serif;
    font-weight: 800; font-size: 22px; color: var(--red); text-transform: uppercase;
  }
  .person-title { font-size: 15px; color: var(--ink); margin-top: 2px; }
  .contact { position: absolute; left: 40px; top: 224px; list-style: none; }
  .contact li {
    display: flex; align-items: center; gap: 9px;
    font-size: 14px; color: var(--ink); line-height: 24px;
  }
  .contact svg { width: 13px; height: 13px; fill: var(--blue-deep); flex: none; }

  .hero-mark {
    position: absolute; right: 36px; top: 50px;
    width: 200px; height: 200px; border-radius: 50%;
    background: var(--red-pale);
    display: flex; align-items: center; justify-content: center;
    font-family: "Montserrat", Arial, sans-serif;
    font-weight: 700; font-size: 28px; color: var(--blue-deep);
  }
</style>
</head>
<body>
  <section class="card card-back" aria-label="Card back">
    <div class="pattern" role="img" aria-label="Tiled pattern of the organisation's symbol in tonal blue"></div>
    <span class="back-mark"><span class="dot"></span>Pinecrest</span>
  </section>

  <section class="card card-front" aria-label="Card front">
    <span class="edge-tab"></span>
    <div class="brand">
      <div class="brand-row">
        <span class="brand-dot"></span>
        <span class="brand-name">Pinecrest</span>
      </div>
      <div class="brand-full">Animal Transfusion Service</div>
    </div>

    <div class="person">
      <div class="person-name">Dana Whitlow</div>
      <div class="person-title">President</div>
    </div>

    <ul class="contact">
      <li>
        <svg viewBox="0 0 24 24" aria-hidden="true"><path d="M6.6 10.8a15.1 15.1 0 0 0 6.6 6.6l2.2-2.2a1 1 0 0 1 1-.25 11.4 11.4 0 0 0 3.6.57 1 1 0 0 1 1 1V20a1 1 0 0 1-1 1A17 17 0 0 1 3 4a1 1 0 0 1 1-1h3.5a1 1 0 0 1 1 1c0 1.25.2 2.46.57 3.6a1 1 0 0 1-.25 1z"/></svg>
        555-014-2290
      </li>
      <li>
        <svg viewBox="0 0 24 24" aria-hidden="true"><path d="M2 5h20v14H2zm2 2v.5l8 5 8-5V7l-8 5z"/></svg>
        dana.whitlow@pinecrestats.com
      </li>
      <li>
        <svg viewBox="0 0 24 24" aria-hidden="true"><path d="M12 2a10 10 0 1 0 0 20 10 10 0 0 0 0-20zm6.9 9h-3a15 15 0 0 0-1.3-5.6A8 8 0 0 1 18.9 11zM12 4.1c.9 1.3 1.7 3.6 1.9 6.9h-3.8c.2-3.3 1-5.6 1.9-6.9zM9.4 5.4A15 15 0 0 0 8.1 11h-3a8 8 0 0 1 4.3-5.6zM5.1 13h3a15 15 0 0 0 1.3 5.6A8 8 0 0 1 5.1 13zm6.9 6.9c-.9-1.3-1.7-3.6-1.9-6.9h3.8c-.2 3.3-1 5.6-1.9 6.9zm2.6-1.3a15 15 0 0 0 1.3-5.6h3a8 8 0 0 1-4.3 5.6z"/></svg>
        www.pinecrestats.com
      </li>
    </ul>

    <div class="hero-mark">Pinecrest</div>
  </section>
</body>
</html>
```